Business Card Design Project

We need a business card design for our IT Managed Services firm.
Our logo is attached.
More information on our company can be found at:
www.dulvarosys.com
Target Market(s)
CEO, President. Mid Size Businesses
Industry/Entity Type
Business

```html
<!DOCTYPE html>
<html lang="en">
<head>
<meta charset="utf-8">
<title>Dulvaro Systems – Business Card</title>
<link rel="stylesheet" href="https://fonts.googleapis.com/css2?family=Arimo:wght@400;700&family=Old+Standard+TT&family=Share+Tech&family=Fredoka:wght@700&display=swap">
<style>
  :root {
    --red: #ee0000;
    --cyan: #00ffff;
    --slate: #4d4d4d;
    --white: #ffffff;
    --ink: #000000;
    --frame: #111111;
  }
  * { box-sizing: border-box; margin: 0; padding: 0; }
  html, body {
    width: 1200px; height: 683px; overflow: hidden;
    background: var(--white);
  }
  .sheet { position: relative; width: 1200px; height: 683px; }

  .card {
    position: absolute;
    width: 575px; height: 328px;
    border: 2px solid var(--frame);
    background: var(--white);
    overflow: hidden;
  }
  .card--red { --accent: var(--red); }
  .card--cyan { --accent: var(--cyan); }
  .pos-tl { left: 1px; top: 1px; }
  .pos-tr { left: 624px; top: 1px; }
  .pos-bl { left: 1px; top: 354px; }
  .pos-br { left: 624px; top: 354px; }

  /* Front */
  .wordmark {
    position: absolute; left: 26px; top: 34px;
    font-family: "Arimo", Arial, sans-serif; font-weight: 700;
    color: var(--ink); line-height: 1;
  }
  .wordmark__name { display: block; font-size: 58px; letter-spacing: -1.5px; }
  .wordmark__sub { display: block; font-size: 12px; margin: 6px 0 0 58px; }

  .name-band {
    position: absolute; left: 0; top: 163px;
    width: 316px; height: 119px;
    background: var(--slate); color: var(--white);
    text-align: right; padding-right: 14px;
  }
  .name-band__name {
    font-family: "Old Standard TT", "Century Schoolbook", serif;
    font-size: 32px; line-height: 1; margin-top: 64px;
  }
  .name-band__title {
    font-family: "Share Tech", sans-serif;
    font-size: 15px; line-height: 1; margin-top: 2px;
  }

  .contact-box {
    position: absolute; left: 328px; top: 163px;
    width: 245px; height: 119px;
    background: var(--accent); color: var(--white);
    font-family: "Arimo", Arial, sans-serif;
    padding: 27px 6px 0 12px;
  }
  .contact-box__line { font-size: 14px; line-height: 17px; }
  .contact-box__address { font-size: 9.5px; line-height: 12px; margin-top: 6px; }

  /* Back */
  .back-fill { position: absolute; inset: 0; background: var(--accent); }
  .web-band {
    position: absolute; left: 0; right: 0; top: 197px; height: 90px;
    background: var(--white);
  }
  .web-band__inner {
    position: absolute; left: 0; right: 0; top: 5px; height: 80px;
    background: var(--slate); color: var(--white);
    font-family: "Fredoka", "Varela Round", sans-serif; font-weight: 700;
    font-size: 30px; letter-spacing: 1px;
    display: flex; align-items: center; justify-content: center;
  }
</style>
</head>
<body>
<main class="sheet">

  <section class="card card--red pos-tl" aria-label="Card front, red">
    <div class="wordmark"><span class="wordmark__name">dulvaro</span><span class="wordmark__sub">Systems, Inc.</span></div>
    <div class="name-band">
      <p class="name-band__name">Abcdef Ghijaklm</p>
      <p class="name-band__title">jhkljh jgjhdhkjfytd</p>
    </div>
    <div class="contact-box">
      <p class="contact-box__line">Phone No: 555-0142-78310</p>
      <p class="contact-box__line">Email: info@dulvarosys.com</p>
      <p class="contact-box__address">Address: 48 Harrow Lane, Suite 210, Brenmoor Park, Westfield 40217</p>
    </div>
  </section>

  <section class="card card--cyan pos-tr" aria-label="Card front, cyan">
    <div class="wordmark"><span class="wordmark__name">dulvaro</span><span class="wordmark__sub">Systems, Inc.</span></div>
    <div class="name-band">
      <p class="name-band__name">Abcdef Ghijaklm</p>
      <p class="name-band__title">jhkljh jgjhdhkjfytd</p>
    </div>
    <div class="contact-box">
      <p class="contact-box__line">Phone No: 555-0142-78310</p>
      <p class="contact-box__line">Email: info@dulvarosys.com</p>
      <p class="contact-box__address">Address: 48 Harrow Lane, Suite 210, Brenmoor Park, Westfield 40217</p>
    </div>
  </section>

  <section class="card card--red pos-bl" aria-label="Card back, red">
    <div class="back-fill"></div>
    <div class="web-band"><div class="web-band__inner">www.dulvarosys.com</div></div>
  </section>

  <section class="card card--cyan pos-br" aria-label="Card back, cyan">
    <div class="back-fill"></div>
    <div class="web-band"><div class="web-band__inner">www.dulvarosys.com</div></div>
  </section>

</main>
</body>
</html>
```